uk based ecommerce website requires fresh look ,high quality look and feel

we are a web based company selling eco friendly ground reinforcement grids to diy and construction sectors
our existing website is www.plumbrookpaving.co.uk ,

we have already updated the logo so that is the branding sorted .so we need a ecommerce website that is very much up-to date in design and layout and which has content management system for ease of use so that we can add products and information as required.

Use current logo as reference for colour scheme.
www.plumbrookpaving.co.uk

The current website has 6 pages accessible through the navigation bar, I would now like 5 pages, removing the need for the Trade Enquiries page possibly have it with along with contact us.

Target Market(s)

construction industry , diy end users,
retail market, landscapers, gardeners

Industry/Entity Type

Construction

Font styles to use
Other font styles liked:
• logo font prometo

Colors
f78f20
9bcb3c

Requirements
Must have
• logo colours and logo design in website with cms responsive design for tablet and mobile devices
• expect content to work flawlessly and look great across all devices
• HTML 5 custom design with coding as required
• must have good experiance in ecommerce website design
• eye catching, high quality look and feel and very user friedly ,very up-to date.
Nice to have
• picture slider show
• explain in writing what exactly i am getting in my ecommerce website
Should not have
• plain , basic design , old fashion looking ,cheap look

```html
<!DOCTYPE html>
<html lang="en">
<head>
<meta charset="utf-8">
<title>About Us – Plumbrook Paving</title>
<link rel="stylesheet" href="https://fonts.googleapis.com/css2?family=Raleway:wght@400;500;600&family=Open+Sans:wght@400;600&display=swap">
<style>
:root{
  --orange:#f78f20;
  --green:#9bcb3c;
  --dark:#2d2d2d;
  --darker:#262626;
  --ink:#333;
  --body:#555;
  --band:#f2f2f2;
  --white:#fff;
}
*{box-sizing:border-box;margin:0;padding:0}
html,body{width:1200px;height:1163px;overflow:hidden}
body{font-family:"Open Sans",sans-serif;color:var(--body);background:var(--white);position:relative}
.wrap{width:1022px;margin:0 auto;position:relative;height:100%}
a{color:inherit;text-decoration:none}

.topbar{height:35px;background:var(--dark);color:var(--white);font-size:12px}
.topbar .wrap{display:flex;align-items:center;justify-content:space-between}
.phones{display:flex;align-items:center;gap:10px}
.phones .sep{width:1px;height:16px;background:#777}
.account{display:flex;align-items:center;gap:6px}

.header{height:75px;background:var(--white)}
.header .wrap{display:flex;align-items:center;justify-content:space-between}
.brand{display:flex;align-items:center;gap:8px}
.brand .mark{width:40px;height:40px;background:var(--green);border-radius:50%}
.brand .name{font-family:"Raleway",sans-serif;font-weight:600;font-size:18px;color:var(--orange);letter-spacing:.5px}
.nav{display:flex;align-items:center;height:100%;font-size:11.6px;color:var(--ink)}
.nav a{padding:0 8px;height:100%;display:flex;align-items:center;position:relative}
.nav a.active::before{content:"";position:absolute;top:0;left:-1px;right:7px;height:3px;background:var(--orange)}
.cart{width:34px;height:34px;border-radius:50%;background:var(--orange);display:flex;align-items:center;justify-content:center;margin-left:7px}

.titleband{height:70px;background:var(--band)}
.titleband .wrap{display:flex;align-items:center;justify-content:space-between}
.titleband h1{font-family:"Raleway",sans-serif;font-weight:400;font-size:28px;color:var(--ink)}
.crumbs{font-size:12px;color:var(--ink)}

.about{position:relative;height:350px}
.photo-back{position:absolute;left:0;top:46px;width:200px;height:189px;background:var(--white);border:1px solid #ddd;padding:7px}
.photo-front{position:absolute;left:95px;top:99px;width:260px;height:186px;background:var(--white);padding:7px;box-shadow:0 2px 6px rgba(0,0,0,.15)}
.frame{position:absolute;left:84px;top:81px;width:253px;height:218px;border:3px solid var(--orange)}
.fill{width:100%;height:100%}
.fill.grid{background:linear-gradient(135deg,#8aa05a,#3a3a3a 45%,#b9b4a8)}
.fill.gravel{background:linear-gradient(160deg,#5b6a86,#a89a86 50%,#c9bca8)}
.copy{position:absolute;left:383px;top:44px;width:650px}
.copy h2{font-family:"Raleway",sans-serif;font-weight:500;font-size:26px;color:var(--ink);line-height:1.2}
.copy h3{font-family:"Raleway",sans-serif;font-weight:400;font-size:16px;color:var(--orange);margin:5px 0 6px}
.copy p{font-size:11.5px;line-height:19.6px;margin-bottom:9px;letter-spacing:-.05px}

.gallery h2{font-family:"Raleway",sans-serif;font-weight:400;font-size:26px;color:var(--ink);text-align:center;height:52px;line-height:34px}
.tiles{display:flex;gap:9px}
.tile{width:248.5px;height:250px;position:relative}
.t1{background:linear-gradient(170deg,#6e8f6a,#3c6fa8 35%,#ddd 55%,#6f6a62)}
.t2{background:var(--orange);display:flex;align-items:center;justify-content:center}
.t2 .plus{width:46px;height:46px;border-radius:50%;background:var(--white);display:flex;align-items:center;justify-content:center}
.t3{background:linear-gradient(180deg,#4d5a2f,#6a5446 40%,#c8c6be 75%,#5f8a2e)}
.t4{background:linear-gradient(180deg,#9fae7c,#c4c0c6 40%,#5e5c66)}

.footer{position:absolute;left:0;top:880px;width:1200px;height:237px;background:var(--dark);color:#ddd}
.footer h4{font-family:"Raleway",sans-serif;font-weight:500;font-size:16px;color:var(--white);padding-bottom:10px;position:relative;margin-bottom:18px}
.footer h4::after{content:"";position:absolute;left:0;bottom:0;width:28px;height:3px;background:var(--orange)}
.col{position:absolute;top:31px}
.c1{left:3px;width:240px}.c2{left:307px}.c3{left:508px}.c4{left:782px;width:230px}
.c1 p{font-size:12px;line-height:19.5px}
.cards{display:flex;gap:6px;margin-top:14px}
.cards span{width:58px;height:33px;border-radius:3px;background:#ececec}
.cards span:nth-child(2){background:#1f3f7a}
.cards span:nth-child(3){background:#1a1a1a;border:1px solid #555}
.cards span:nth-child(4){background:#fff3d6}
.links{list-style:none;font-size:12px;line-height:24px}
.contact{display:flex;align-items:center;gap:8px;font-size:14px;color:var(--white);margin-bottom:12px}
.contact .ic{width:28px;height:28px;background:var(--orange);display:flex;align-items:center;justify-content:center}
.email-in{width:230px;height:36px;background:var(--white);font-size:12px;color:#777;padding:0 12px;display:flex;align-items:center;margin-top:-3px}
.send{width:114px;height:36px;background:var(--orange);color:var(--white);font-size:12px;display:flex;align-items:center;justify-content:center;margin-top:9px}

.bottombar{position:absolute;left:0;top:1117px;width:1200px;height:46px;background:var(--darker);color:var(--white);font-size:12px}
.bottombar .wrap{display:flex;align-items:center}
.bottombar p{margin-left:3px}
.totop{position:absolute;left:1068px;top:1096px;width:48px;height:48px;border-radius:50%;background:var(--white);border:1px solid #ddd;display:flex;align-items:center;justify-content:center}
</style>
</head>
<body>
<div class="topbar">
  <div class="wrap">
    <div class="phones">
      <svg width="14" height="14" viewBox="0 0 24 24"><path fill="#fff" d="M6.6 10.8a15 15 0 0 0 6.6 6.6l2.2-2.2c.3-.3.7-.4 1-.2 1.1.4 2.3.6 3.6.6.6 0 1 .4 1 1V20c0 .6-.4 1-1 1A17 17 0 0 1 3 4c0-.6.4-1 1-1h3.5c.6 0 1 .4 1 1 0 1.3.2 2.5.6 3.6.1.3 0 .7-.2 1z"/></svg>
      <span>0123-456-7890</span><span class="sep"></span><span>0800-555-0142</span>
    </div>
    <div class="account">
      <a href="#">Login</a><span>|</span><a href="#">Register</a>
      <svg width="14" height="14" viewBox="0 0 24 24" style="margin-left:8px"><circle cx="10" cy="10" r="6" fill="none" stroke="#fff" stroke-width="2.4"/><path d="M14.5 14.5 20 20" stroke="#fff" stroke-width="2.4"/></svg>
    </div>
  </div>
</div>

<header class="header">
  <div class="wrap">
    <div class="brand"><span class="mark"></span><span class="name">PLUMBROOK PAVING</span></div>
    <nav class="nav">
      <a href="#" class="active">SHOP</a>
      <a href="#">ABOUT US</a>
      <a href="#">GROUND SOLUTIONS</a>
      <a href="#">PLUMBROOK</a>
      <a href="#">CONTACT US</a>
      <span class="cart"><svg width="18" height="18" viewBox="0 0 24 24"><path fill="#fff" d="M7 18a2 2 0 1 0 0 4 2 2 0 0 0 0-4zm10 0a2 2 0 1 0 0 4 2 2 0 0 0 0-4zM1 2v2h2l3.6 7.6-1.4 2.4c-.5 1 .2 2 1.3 2H19v-2H7.4l1.1-2h7.5c.8 0 1.4-.4 1.7-1l3.6-6.5L19.6 4H5.2l-.9-2z"/></svg></span>
    </nav>
  </div>
</header>

<section class="titleband">
  <div class="wrap">
    <h1>About Us</h1>
    <div class="crumbs">Home / About Us</div>
  </div>
</section>

<section class="about">
  <div class="wrap">
    <div class="photo-back"><div class="fill grid" role="img" aria-label="Grass edge beside a black ground reinforcement grid"></div></div>
    <div class="frame"></div>
    <div class="photo-front"><div class="fill gravel" role="img" aria-label="Wheeled walker rolling over a contained gravel path"></div></div>
    <div class="copy">
      <h2>Contained Gravel For Parking and Pathways</h2>
      <h3>Affordable And Green Solutions For Flood Prevention</h3>
      <p>Plumbrook is a family run company that specialises in stabilisation grid systems for gravel and grass surfaces. Our main focus is to provide Quality products at an affordable price and which meets the requirements of our customers. We supply a permeable paving system that keeps the traditional look of a gravel driveway, but gives it the more advanced and eco-logical approach of a contained gravel system All installations of all landscaping of driveways projects require to incorpo-rate the SUDS techniques which is Sustainable Urban Drainage Systems.</p>
      <p>We supply all that's required to install an eco friendly system without any harmful chemicals. Our material will not harm the environment or require planning permission. All our systems are self-draining.</p>
      <p>We would advise the use of a geotextile layer beneath the paver as filtration and suppressant &nbsp;and also to stop the gravel reduction this method should also in most cases remove any need for the extra expense of any drainage system and labour related costs involved.</p>
    </div>
  </div>
</section>

<section class="gallery">
  <div class="wrap">
    <h2>Our Gallery</h2>
    <div class="tiles">
      <div class="tile t1" role="img" aria-label="Boats on trailers parked on a gravel grid"></div>
      <div class="tile t2" role="img" aria-label="Close view of a gravel filled grid">
        <span class="plus"><svg width="20" height="20" viewBox="0 0 20 20"><path d="M10 2v16M2 10h16" stroke="#f78f20" stroke-width="2"/></svg></span>
      </div>
      <div class="tile t3" role="img" aria-label="Gravel driveway leading to a brick house"></div>
      <div class="tile t4" role="img" aria-label="Empty white grid panels laid out on site"></div>
    </div>
  </div>
</section>

<footer class="footer">
  <div class="wrap">
    <div class="col c1">
      <h4>About Us</h4>
      <p>Lorem Ipsum is simply dummy text of the printing and typesetting industry. Lorem Ipsum has been the industry's standard dummy text ever since the 1500s</p>
      <div class="cards"><span></span><span></span><span></span><span></span></div>
    </div>
    <div class="col c2">
      <h4>Useful Links</h4>
      <ul class="links"><li>Site Map</li><li>Email</li><li>Privacy Policy</li><li>Terms of Service</li><li>Delivery and Returns</li></ul>
    </div>
    <div class="col c3">
      <h4>Get In Touch</h4>
      <div class="contact"><span class="ic"><svg width="12" height="12" viewBox="0 0 24 24"><path fill="#fff" d="M6.6 10.8a15 15 0 0 0 6.6 6.6l2.2-2.2c.3-.3.7-.4 1-.2 1.1.4 2.3.6 3.6.6.6 0 1 .4 1 1V20c0 .6-.4 1-1 1A17 17 0 0 1 3 4c0-.6.4-1 1-1h3.5c.6 0 1 .4 1 1 0 1.3.2 2.5.6 3.6.1.3 0 .7-.2 1z"/></svg></span>0123-456-7890</div>
      <div class="contact"><span class="ic"><svg width="13" height="10" viewBox="0 0 13 10"><rect x=".5" y=".5" width="12" height="9" fill="none" stroke="#fff"/><path d="M.5.5 6.5 6l6-5.5" fill="none" stroke="#fff"/></svg></span>sales@plumbrookpaving.co.uk</div>
    </div>
    <div class="col c4">
      <h4>Newsletter</h4>
      <div class="email-in">Email</div>
      <div class="send">SEND</div>
    </div>
  </div>
</footer>

<div class="bottombar"><div class="wrap"><p>© 2016 All Rights Reserved</p></div></div>
<a class="totop" href="#"><svg width="12" height="8" viewBox="0 0 12 8"><path d="M2 6 6 2l4 4" fill="none" stroke="#f78f20" stroke-width="2"/></svg></a>
</body>
</html>
```